Pediatric Therapy Clinic Brochure

We need a Brochure for a new pediatric therapy clinic. The clinic offers occupational therapy, physical therapy, speech therapy and feeding therapy. We want a brochure for parents, doctors and medical professional. It should have a fun and inviting, but still professional feel. Should be kid focused, bright and colorful. All the text / wording is there and a rough layout. Now I need someone to tidy and jazz it up and make it look professional.

Target Market(s)

Parents, doctors, medical professional

Industry/Entity Type

Medical

Font styles to use
Serif
Sans Serif

Requirements
Must have
• Keep All the text with information about services the same. Logo on front. Pictures throughout (use any of the pictures provided) (try and match up with corresponding service) (pictures are labeled). Need to have Map and contact info
• Keep colors consistent with our logo
Nice to have
• Background, special effects. Make it look fancy and professional
Should not have
• Not so busy that is takes away from the text

```html
<!DOCTYPE html>
<html lang="en">
<head>
<meta charset="utf-8">
<title>Cedar Ridge Pediatric Therapy – Trifold Brochure</title>
<link href="https://fonts.googleapis.com/css2?family=Lato:wght@400;700;900&display=swap" rel="stylesheet">
<style>
:root{
  --navy:#1f5f99;
  --navy-dark:#174a7a;
  --orange:#f26a1b;
  --green:#8cc63f;
  --green-dark:#6fae2a;
  --sky:#cfe6f7;
  --sky-light:#eef6fc;
  --page:#e6e6e6;
  --ink:#33475b;
  --white:#ffffff;
}
*{box-sizing:border-box;margin:0;padding:0}
html,body{width:932px;height:1200px;overflow:hidden}
body{background:var(--page);font-family:"Lato",sans-serif;color:var(--ink);position:relative}
.brochure{position:absolute;left:16px;top:282px;width:900px;height:636px;display:flex;box-shadow:0 6px 18px rgba(0,0,0,.18)}
.panel{position:relative;width:300px;height:636px;overflow:hidden}
.panel--about{background:linear-gradient(180deg,#bfe0f6 0%,var(--sky-light) 60%,#f7fbfe 100%)}
.panel--contact{background:linear-gradient(180deg,#c2e1f6 0%,#d9ecf9 55%,#e9f4fc 100%)}
.panel--cover{background:var(--white)}
.about-text{position:absolute;left:22px;top:22px;width:258px;font-size:10.6px;line-height:16.6px;text-align:justify;color:var(--ink)}
.pill{position:absolute;border-radius:18px;color:var(--white);font-weight:700;text-align:center;letter-spacing:.2px}
.pill--navy{left:22px;top:325px;width:256px;height:32px;line-height:32px;background:var(--navy);font-size:19px;box-shadow:0 2px 3px rgba(0,0,0,.2)}
.pill--orange{left:55px;top:333px;width:190px;height:28px;line-height:28px;background:var(--orange);font-size:18px;box-shadow:0 2px 3px rgba(0,0,0,.2)}
.about-sub{position:absolute;left:0;top:370px;width:300px;text-align:center;font-size:12.5px;line-height:16px;color:var(--navy-dark)}
.photo{position:absolute}
.photo--kids{left:0;top:412px;width:300px;height:184px;background:linear-gradient(90deg,#e9a9c4 0%,#f3c9a0 35%,#7fb3de 60%,#f5d36b 100%);opacity:.9}
.band-green{position:absolute;left:0;bottom:0;width:300px;background:var(--green);color:var(--white);text-align:center}
.band-green--about{height:40px;padding-top:4px;font-size:11px;line-height:15px}
.band-green--about strong{font-size:12px}
.band-green--contact{height:33px;line-height:33px;font-size:11.5px}
.map-ring{position:absolute;left:54px;top:21px;width:192px;height:192px;border-radius:50%;border:4px solid var(--navy);background:var(--white);padding:4px;box-shadow:0 0 0 2px #fff,0 0 0 3px #9fc4e4}
.map{width:100%;height:100%;border-radius:50%;background:linear-gradient(135deg,#dcdcdc 0%,#efefef 50%,#d6d0c4 100%)}
.brand{position:absolute;display:flex;align-items:center;gap:8px;color:var(--navy)}
.brand-dot{width:16px;height:16px;border-radius:50%;background:var(--orange);flex:none}
.brand-name{font-weight:900;font-size:26px;line-height:26px}
.brand-name small{display:block;font-size:14px;line-height:16px;letter-spacing:.6px}
.brand--contact{left:40px;top:256px}
.brand--cover{left:38px;top:40px}
.contact-list{position:absolute;left:0;top:374px;width:300px;text-align:center;font-size:12.5px;line-height:17px;color:var(--ink)}
.contact-item{display:flex;flex-direction:column;align-items:center}
.contact-item svg{margin-bottom:6px}
.contact-item + .contact-item{margin-top:12px}
.visit{position:absolute;left:0;top:580px;width:300px;text-align:center;font-size:11.5px}
.quote-band{position:absolute;left:0;top:117px;width:300px;height:62px;background:var(--orange);color:var(--white);text-align:center;font-size:12.5px;line-height:15.5px;padding-top:8px;text-transform:uppercase}
.photo--child{left:0;top:179px;width:300px;height:298px;background:radial-gradient(circle at 55% 55%,#f6d8b8 0%,#f2c43a 35%,#3b8ad6 65%,#e94141 100%)}
.services{position:absolute;left:0;top:477px;width:300px;height:126px;background:var(--navy);color:var(--white);padding:16px 10px 0 14px;display:grid;grid-template-columns:134px 1fr;row-gap:7px;font-size:12.5px;line-height:16px;list-style:none}
.services li{display:flex;gap:5px}
.services li::before{content:"";flex:none;width:8px;height:8px;border:1.5px solid var(--white);border-radius:50%;margin-top:4px}
.cover-phone{position:absolute;left:0;bottom:0;width:300px;height:33px;display:flex;align-items:center;justify-content:center;gap:8px;color:var(--orange);font-weight:700;font-size:20px}
</style>
</head>
<body>
<main class="brochure">

  <section class="panel panel--about">
    <p class="about-text">We are a team of highly trained pediatric therapists located in North Riverton. We are dedicated to helping children and adolescents along with their families with a full scope of therapy services, including occupational therapy, physical therapy, speech therapy, feeding therapy, sensory integration therapy, and group classes to meet the needs of all children. When you walk into our clinic you will see climbing walls, bikes, suspension swings, a trampoline and quiet areas where children are achieving complex and interdisciplinary skills while having fun! Our mission is to provide compassionate and high quality therapy services in an enriching and enjoyable environment where all children thrive!</p>
    <div class="pill pill--navy">CONTACT US TODAY</div>
    <p class="about-sub">and learn which therapy would be<br>most appropriate for your child.</p>
    <div class="photo photo--kids" role="img" aria-label="Photo of smiling children lying on the floor with flowers and trees"></div>
    <div class="band-green band-green--about">www.cedarridgetherapy.com<br><strong>555.204.7316</strong></div>
  </section>

  <section class="panel panel--contact">
    <div class="map-ring"><div class="map" role="img" aria-label="Street map showing the clinic location"></div></div>
    <div class="brand brand--contact"><span class="brand-dot"></span><span class="brand-name">Cedar Ridge<small>PEDIATRIC THERAPY</small></span></div>
    <div class="pill pill--orange">CONTACT US!</div>
    <div class="contact-list">
      <div class="contact-item">
        <svg width="18" height="18" viewBox="0 0 18 18" aria-hidden="true"><circle cx="9" cy="9" r="8" fill="none" stroke="#1f5f99" stroke-width="1.5"/><path d="M9 4.5a3 3 0 0 1 3 3c0 2.2-3 5.5-3 5.5s-3-3.3-3-5.5a3 3 0 0 1 3-3z" fill="#1f5f99"/><circle cx="9" cy="7.5" r="1" fill="#fff"/></svg>
        <span>Cedar Ridge Pediatric Therapy<br>1870 W. Maple Ave. Suite 210<br>Riverton, AZ 85099</span>
      </div>
      <div class="contact-item">
        <svg width="18" height="18" viewBox="0 0 18 18" aria-hidden="true"><circle cx="9" cy="9" r="8" fill="none" stroke="#1f5f99" stroke-width="1.5"/><rect x="5" y="7" width="8" height="5" rx="1" fill="#1f5f99"/><path d="M5 7.5q4-3 8 0" stroke="#1f5f99" stroke-width="1.5" fill="none"/></svg>
        <span>555.204.7316</span>
      </div>
      <div class="contact-item">
        <svg width="18" height="18" viewBox="0 0 18 18" aria-hidden="true"><circle cx="9" cy="9" r="8" fill="none" stroke="#1f5f99" stroke-width="1.5"/><rect x="5" y="6" width="8" height="6" fill="#1f5f99"/><path d="M5 6l4 3.5L13 6" stroke="#fff" stroke-width="1" fill="none"/></svg>
        <span>hello@cedarridgetherapy.com</span>
      </div>
    </div>
    <p class="visit">Visit us online:</p>
    <div class="band-green band-green--contact">www.cedarridgetherapy.com</div>
  </section>

  <section class="panel panel--cover">
    <div class="brand brand--cover"><span class="brand-dot"></span><span class="brand-name">Cedar Ridge<small>PEDIATRIC THERAPY</small></span></div>
    <p class="quote-band">Every child is gifted.<br>They just unwrap their packages<br>at different times.</p>
    <div class="photo photo--child" role="img" aria-label="Photo of a smiling toddler in a yellow shirt in a colourful ball pit"></div>
    <ul class="services">
      <li>Speech Therapy</li>
      <li>Feeding Therapy</li>
      <li>Occupational Therapy</li>
      <li>Sensory Integration Therapy</li>
      <li>Physical Therapy</li>
      <li>Group Therapy</li>
    </ul>
    <div class="cover-phone">
      <svg width="18" height="18" viewBox="0 0 18 18" aria-hidden="true"><circle cx="9" cy="9" r="8" fill="none" stroke="#f26a1b" stroke-width="1.5"/><path d="M6 5.5l1.5-.5 1 2-1 .8a5 5 0 0 0 2.7 2.7l.8-1 2 1-.5 1.5c-3.5 0-6.5-3-6.5-6.5z" fill="#f26a1b"/></svg>
      <span>555.204.7316</span>
    </div>
  </section>

</main>
</body>
</html>
```